Monthly Report PowerPoint Template

We are looking for a set of slides to use as a template for a report that we send out monthly on the state of the solar and storage market. It should be professional and low profile, attached are the slides we currently use/would like to replace: 1) title slide, 2) content summary, 3) content, and 4) section break. We are mainly concerned about a new design for 2), we are using the basic PowerPoint table and would like both a new table style and a version that is more visual. Thanks!

Requirements
Must have
• Light theme
Should not have
• No stock images

```html
<!DOCTYPE html>
<html lang="en">
<head>
<meta charset="utf-8">
<title>Voltline Insights – Monthly Report Slides</title>
<link rel="stylesheet" href="https://fonts.googleapis.com/css2?family=Orbitron:wght@800;900&family=Poppins:ital,wght@0,400;0,500;0,600;1,500;1,600&display=swap">
<style>
  :root{
    --stage:#2d2d2d;
    --blue:#0b6aa0;
    --blue-deep:#0a5f91;
    --orange:#f5a01a;
    --orange-soft:#f0a22e;
    --row-tint:#c5e5f5;
    --sky:#bfe2f3;
    --logo-light:#a8d8f0;
    --ink:#1b2233;
    --white:#ffffff;
    --grid:#d9d9d9;
    --placeholder-top:#e6ebf0;
    --placeholder-bottom:#cfd6dd;
  }
  *{box-sizing:border-box;margin:0;padding:0}
  html,body{width:1200px;height:1200px;overflow:hidden;background:var(--stage)}
  body{position:relative;font-family:'Poppins',sans-serif}

  .slide{position:absolute;width:905px;height:603px;background:var(--white);overflow:hidden;
    transform:scale(0.6212);transform-origin:0 0}
  .slide--title{left:26.7px;top:165.8px}
  .slide--summary{left:611.8px;top:165.8px}
  .slide--section{left:26.7px;top:575.8px}
  .slide--content{left:611.8px;top:575.8px}

  .frame{position:absolute;inset:0;width:905px;height:603px}

  .brand{position:absolute;display:flex;align-items:center;gap:8px;
    font-family:'Poppins',sans-serif;font-weight:500;font-size:25px;color:var(--blue-deep);white-space:nowrap}
  .brand__dot{width:20px;height:20px;border-radius:50%;background:currentColor}
  .brand--light{color:var(--logo-light)}

  /* title slide */
  .photo{position:absolute;inset:0;background:linear-gradient(180deg,#7fb3dc 0%,#a9c9e2 12%,#6f7d74 22%,#3a4f7a 45%,#23366b 100%)}
  .title-block{position:absolute;right:22px;top:249px;text-align:right;
    font-family:'Orbitron',sans-serif;font-weight:900;font-size:38px;line-height:54px;color:var(--white);
    letter-spacing:1px;white-space:nowrap}
  .title-sub{position:absolute;right:33px;top:392px;font-weight:600;font-size:21px;color:var(--white)}

  /* ribbons */
  .ribbon-text{position:absolute;left:15px;font-family:'Orbitron',sans-serif;font-weight:900;color:var(--white);
    letter-spacing:1px;white-space:nowrap}
  .ribbon-text--summary{top:43px;font-size:30px;line-height:46px}
  .ribbon-text--content{top:71px;font-size:23px;line-height:48px}

  /* table */
  .report-table{position:absolute;left:61px;top:118px;width:783px;border-collapse:collapse;font-size:14px;color:var(--ink)}
  .report-table th{background:var(--blue);color:var(--white);font-style:italic;font-weight:600;font-size:17px;
    height:56px;text-align:left}
  .report-table td{height:56px}
  .report-table tbody tr:nth-child(odd){background:var(--row-tint)}
  .col-sl{width:112px;padding-left:29px}
  .col-desc{width:335px}
  .col-price{width:126px;padding-left:11px}
  .col-qty{width:107px;padding-left:16px}
  .col-total{padding-left:6px}
  td.col-sl,td.col-price,td.col-total{font-style:italic;font-weight:500}
  td.col-sl{padding-left:37px}
  td.col-price{padding-left:17px}
  td.col-qty{padding-left:20px;font-size:12px}
  td.col-total{padding-left:12px}

  /* section slide */
  .section-visual{position:absolute;left:279px;top:123px;width:295px;height:196px;
    background:linear-gradient(180deg,var(--placeholder-top),var(--placeholder-bottom))}
  .section-title{position:absolute;left:0;width:905px;top:363px;text-align:center;
    font-family:'Orbitron',sans-serif;font-weight:900;font-size:42px;line-height:50px;color:var(--blue);letter-spacing:1px}

  /* content slide */
  .body-copy{position:absolute;left:61px;width:785px;font-size:12.2px;line-height:14.5px;color:var(--ink)}
</style>
</head>
<body>

<!-- Title slide -->
<section class="slide slide--title">
  <div class="photo" role="img" aria-label="Photo of rows of solar panels in a field under a blue sky"></div>
  <svg class="frame" viewBox="0 0 905 603" aria-hidden="true">
    <polygon points="522,0 905,0 905,603 410,603" fill="var(--blue)"/>
    <polygon points="466,0 486,0 376,603 356,603" fill="var(--blue)"/>
    <polygon points="490,0 503,0 392,603 375,603" fill="var(--orange)"/>
    <polygon points="352,375 370,375 320,603 300,603" fill="var(--orange)"/>
    <polygon points="413,227 905,227 905,375 383,375" fill="var(--orange)"/>
  </svg>
  <div class="brand brand--light" style="right:33px;top:30px"><span class="brand__dot"></span>Voltline Insights</div>
  <h1 class="title-block">VOLTLINE INSIGHTS<br>APRIL UPDATE</h1>
  <p class="title-sub">Residential and Commercial Solar</p>
</section>

<!-- Content summary slide -->
<section class="slide slide--summary">
  <svg class="frame" viewBox="0 0 905 603" aria-hidden="true">
    <polygon points="462,0 905,0 905,24 485,24" fill="var(--orange-soft)"/>
    <polygon points="0,13 466,13 477,24 0,24" fill="var(--blue)"/>
    <polygon points="0,591 455,591 443,603 0,603" fill="var(--blue)"/>
    <polygon points="463,591 905,591 905,603 451,603" fill="var(--orange-soft)"/>
    <polygon points="0,43 567,43 595,89 0,89" fill="var(--orange)"/>
  </svg>
  <h2 class="ribbon-text ribbon-text--summary">REPORT CONTENT SUMMARY</h2>
  <div class="brand" style="right:63px;top:46px"><span class="brand__dot"></span>Voltline Insights</div>
  <table class="report-table">
    <thead>
      <tr><th class="col-sl">SL.</th><th class="col-desc">PLANT DESCRIPTION</th><th class="col-price">PRICE</th><th class="col-qty">QTY.</th><th class="col-total">TOTAL</th></tr>
    </thead>
    <tbody>
      <tr><td class="col-sl">1</td><td class="col-desc">Lorem ipsum</td><td class="col-price">$10</td><td class="col-qty">1</td><td class="col-total">$10</td></tr>
      <tr><td class="col-sl">2</td><td class="col-desc">Consectetur adipiscing elit</td><td class="col-price">$10</td><td class="col-qty">1</td><td class="col-total">$10</td></tr>
      <tr><td class="col-sl">3</td><td class="col-desc">Duis aute irure dolor</td><td class="col-price">$10</td><td class="col-qty">1</td><td class="col-total">$10</td></tr>
      <tr><td class="col-sl">4</td><td class="col-desc">Lorem ipsum</td><td class="col-price">$10</td><td class="col-qty">1</td><td class="col-total">$10</td></tr>
      <tr><td class="col-sl">5</td><td class="col-desc">Consectetur adipiscing elit</td><td class="col-price">$10</td><td class="col-qty">1</td><td class="col-total">$10</td></tr>
      <tr><td class="col-sl">6</td><td class="col-desc">Duis aute irure dolor</td><td class="col-price">$10</td><td class="col-qty">1</td><td class="col-total">$10</td></tr>
      <tr><td class="col-sl">7</td><td class="col-desc">Lorem ipsum</td><td class="col-price">$10</td><td class="col-qty">1</td><td class="col-total">$10</td></tr>
    </tbody>
  </table>
</section>

<!-- Section break slide -->
<section class="slide slide--section">
  <svg class="frame" viewBox="0 0 905 603" aria-hidden="true">
    <polygon points="462,0 905,0 905,24 485,24" fill="var(--orange-soft)"/>
    <polygon points="0,13 466,13 477,24 0,24" fill="var(--blue)"/>
    <polygon points="0,591 455,591 443,603 0,603" fill="var(--blue)"/>
    <polygon points="463,591 905,591 905,603 451,603" fill="var(--orange-soft)"/>
  </svg>
  <div class="brand" style="right:65px;top:45px"><span class="brand__dot"></span>Voltline Insights</div>
  <div class="section-visual" role="img" aria-label="Image area: house with rooftop solar panels"></div>
  <svg class="frame" viewBox="0 0 905 603" aria-hidden="true">
    <circle cx="597" cy="263" r="66" fill="var(--blue)"/>
    <g fill="var(--white)">
      <rect x="557" y="287" width="7" height="4"/>
      <rect x="570" y="280" width="8" height="11"/>
      <rect x="584" y="272" width="8" height="19"/>
      <rect x="598" y="262" width="8" height="29"/>
      <rect x="612" y="250" width="8" height="41"/>
      <rect x="626" y="238" width="8" height="53"/>
    </g>
    <path d="M556,280 Q600,270 626,230" fill="none" stroke="var(--white)" stroke-width="4" stroke-linecap="round"/>
    <polygon points="631,222 632,238 619,230" fill="var(--white)"/>
  </svg>
  <h2 class="section-title">RESIDENTIAL SOLAR:<br>MARKET DEMAND TRENDS</h2>
</section>

<!-- Content slide -->
<section class="slide slide--content">
  <svg class="frame" viewBox="0 0 905 603" aria-hidden="true">
    <polygon points="462,0 905,0 905,24 485,24" fill="var(--orange-soft)"/>
    <polygon points="0,13 466,13 477,24 0,24" fill="var(--blue)"/>
    <polygon points="0,591 455,591 443,603 0,603" fill="var(--blue)"/>
    <polygon points="463,591 905,591 905,603 451,603" fill="var(--orange-soft)"/>
    <polygon points="0,71 740,71 770,119 0,119" fill="var(--orange)"/>
  </svg>
  <h2 class="ribbon-text ribbon-text--content">MONTHLY RESIDENTIAL PERMITS ISSUED TRENDS</h2>
  <p class="body-copy" style="top:143px">Lorem ipsum dolor sit amet, consectetur adipiscing elit, sed do eiusmod tempor incididunt ut labore et dolore magna aliqua. Quis ipsum suspendisse ultrices gravida. Risus commodo viverra maecenas accumsan lacus vel facilisis. Lorem ipsum dolor sit amet, consectetur adipiscing elit, sed do eiusmod tempor incididunt ut labore et dolore magna aliqua. Quis ipsum suspendisse ultrices gravida. Risus commodo viverra maecenas accumsan lacus vel facilisis. Lorem ipsum dolor sit amet, consectetur adipiscing elit, sed do eiusmod tempor incididunt ut labore et dolore magna aliqua. Quis ipsum suspendisse ultrices gravida. Risus commodo viverra maecenas accumsan lacus vel facilisis.</p>
  <p class="body-copy" style="top:244px">Lorem ipsum dolor sit amet, consectetur adipiscing elit, sed do eiusmod tempor incididunt ut labore et dolore magna aliqua. Quis ipsum suspendisse ultrices gravida. Risus commodo viverra maecenas accumsan lacus vel facilisis. Lorem ipsum dolor sit amet, consectetur adipiscing elit, sed do eiusmod tempor incididunt ut labore et dolore magna aliqua. Quis ipsum suspendisse ultrices gravida. Risus commodo viverra maecenas accumsan lacus vel facilisis.</p>
  <svg class="frame" viewBox="0 0 905 603" role="img" aria-label="Bar chart of monthly residential permits in three groups">
    <g stroke="var(--grid)" stroke-width="1">
      <path d="M280,353H620M280,378H620M280,403H620M280,428H620M280,453H620M280,478H620M280,503H620M280,528H620M280,553H620"/>
      <path d="M302,353V568M327,353V568M352,353V568M377,353V568M402,353V568M427,353V568M452,353V568M477,353V568M502,353V568M527,353V568M552,353V568M577,353V568M602,353V568"/>
    </g>
    <rect x="302" y="443" width="25" height="125" fill="var(--orange-soft)"/>
    <rect x="327" y="393" width="25" height="175" fill="var(--sky)"/>
    <rect x="352" y="493" width="25" height="75" fill="var(--blue)"/>
    <rect x="402" y="468" width="25" height="100" fill="var(--orange-soft)"/>
    <rect x="427" y="443" width="25" height="125" fill="var(--sky)"/>
    <rect x="452" y="418" width="25" height="150" fill="var(--blue)"/>
    <rect x="503" y="393" width="25" height="175" fill="var(--orange-soft)"/>
    <rect x="528" y="443" width="25" height="125" fill="var(--sky)"/>
    <rect x="553" y="418" width="25" height="150" fill="var(--blue)"/>
    <path d="M277,340V568H626" stroke="#111" stroke-width="2.5" fill="none"/>
    <polygon points="277,331 272,342 282,342" fill="#111"/>
    <polygon points="634,568 623,563 623,573" fill="#111"/>
  </svg>
  <div class="brand" style="right:43px;top:537px"><span class="brand__dot"></span>Voltline Insights</div>
</section>

</body>
</html>
```